We are a family based professional house keeping and cleaning services company. we offer 30% off for the first cleaning to any new costumer with this post cards, we offer the best service in town 100% guaranteed or money backsome of the services we offer includemove in/out cleaningdeep cleaning in every visitsteam cleaningspecial event cleaningpersonalized cleaning to cover every costumer needs and any requestcontact info phone 513-630-6275email tidyhomesquad42@maplenest.com
Target Market(s)
middle and upper class
Industry/Entity Type
It Company
Colors
Designer to choose colors to be used in the design.
Look and feel

```html
<!DOCTYPE html>
<html lang="en">
<head>
<meta charset="utf-8">
<title>We Clean, You Relax – Postcard</title>
<link rel="stylesheet" href="https://fonts.googleapis.com/css2?family=Montserrat:ital,wght@0,600;0,700;0,800;1,700;1,800&family=Oswald:wght@500;600&family=Roboto+Condensed:wght@400;700&display=swap">
<style>
  :root {
    --brand-blue: #2f5fae;
    --brand-blue-deep: #244f99;
    --ink-blue: #1f5aa6;
    --white: #ffffff;
    --band: #e9edf4;
    --yellow: #f7ea2a;
    --teal: #19b3d3;
    --teal-dark: #137f8a;
    --discount-ink: #1d6a6a;
    --discount-green: #3c9a3d;
    --photo-warm-1: #efe6dc;
    --photo-warm-2: #c9b8a6;
  }
  * { margin: 0; padding: 0; box-sizing: border-box; }
  html, body { width: 1200px; height: 667px; overflow: hidden; background: var(--white); }
  .postcard { position: relative; width: 1200px; height: 667px; overflow: hidden; font-family: "Montserrat", sans-serif; }
  .family-photo {
    position: absolute; left: 0; top: 0; width: 700px; height: 667px;
    background: radial-gradient(ellipse at 40% 55%, #b9c6d8 0%, transparent 45%),
                linear-gradient(160deg, var(--photo-warm-1) 0%, #e3d6c8 50%, var(--photo-warm-2) 100%);
  }
  .blue-panel { position: absolute; inset: 0; width: 1200px; height: 667px; }
  .headline {
    position: absolute; left: 492px; top: 78px;
    font-weight: 800; font-size: 50px; letter-spacing: 1px; color: var(--white); line-height: 1;
  }
  .tagline {
    position: absolute; left: 494px; top: 143px; width: 640px;
    font-style: italic; font-weight: 800; font-size: 21px; line-height: 30px; color: var(--white);
  }
  .services { position: absolute; left: 600px; top: 234px; list-style: none; }
  .services li {
    display: flex; align-items: center; gap: 12px; height: 39px;
    font-weight: 700; font-size: 19px; color: var(--white);
  }
  .services svg { width: 25px; height: 25px; flex: none; }
  .discount-badge { position: absolute; left: 586px; top: 400px; width: 280px; height: 170px; }
  .discount-word { font-family: "Oswald", sans-serif; font-weight: 600; font-size: 35px; fill: var(--discount-ink); }
  .discount-sub { font-family: "Montserrat", sans-serif; font-weight: 600; font-size: 15px; fill: var(--discount-green); }
  .discount-pct { font-family: "Oswald", sans-serif; font-weight: 500; font-size: 27px; fill: var(--white); }
  .offer-note {
    position: absolute; left: 864px; top: 459px; width: 300px;
    font-style: italic; font-weight: 700; font-size: 15.5px; line-height: 19px; color: var(--white);
  }
  .contact-band {
    position: absolute; left: 0; top: 561px; width: 1200px; height: 69px; background: var(--band);
  }
  .contact {
    position: absolute; top: 578px; display: flex; align-items: center; gap: 26px;
    font-family: "Roboto Condensed", sans-serif; font-weight: 700; font-size: 27px; color: var(--ink-blue);
  }
  .contact-phone { left: 106px; }
  .contact-email { left: 521px; }
  .contact svg { width: 40px; height: 36px; flex: none; }
</style>
</head>
<body>
<main class="postcard">
  <div class="family-photo" role="img" aria-label="Smiling family of three — mother, father and toddler — in a bright living room"></div>

  <svg class="blue-panel" viewBox="0 0 1200 667" aria-hidden="true">
    <defs>
      <linearGradient id="panelShade" x1="0" y1="0" x2="1" y2="1">
        <stop offset="0" stop-color="#3565b3"/>
        <stop offset="1" stop-color="#2a57a3"/>
      </linearGradient>
    </defs>
    <path d="M455 0 H1200 V667 H585 C500 470 430 230 455 0 Z" fill="url(#panelShade)"/>
  </svg>

  <h1 class="headline">WE CLEAN, YOU RELAX!</h1>
  <p class="tagline">Family based professional house keeping and cleaning services that you can trust.</p>

  <ul class="services">
    <li><svg viewBox="0 0 24 24"><circle cx="12" cy="12" r="11" fill="var(--yellow)"/><path d="M6.5 12.5l3.6 3.6 7.4-8" fill="none" stroke="var(--brand-blue-deep)" stroke-width="2.8" stroke-linecap="round" stroke-linejoin="round"/></svg>Move in/out cleaning</li>
    <li><svg viewBox="0 0 24 24"><circle cx="12" cy="12" r="11" fill="var(--yellow)"/><path d="M6.5 12.5l3.6 3.6 7.4-8" fill="none" stroke="var(--brand-blue-deep)" stroke-width="2.8" stroke-linecap="round" stroke-linejoin="round"/></svg>Deep cleaning in every visit</li>
    <li><svg viewBox="0 0 24 24"><circle cx="12" cy="12" r="11" fill="var(--yellow)"/><path d="M6.5 12.5l3.6 3.6 7.4-8" fill="none" stroke="var(--brand-blue-deep)" stroke-width="2.8" stroke-linecap="round" stroke-linejoin="round"/></svg>Special event cleaning</li>
    <li><svg viewBox="0 0 24 24"><circle cx="12" cy="12" r="11" fill="var(--yellow)"/><path d="M6.5 12.5l3.6 3.6 7.4-8" fill="none" stroke="var(--brand-blue-deep)" stroke-width="2.8" stroke-linecap="round" stroke-linejoin="round"/></svg>Personalized cleaning covering costumer needs</li>
  </ul>

  <svg class="discount-badge" viewBox="0 0 280 170" aria-label="30% discount for the first cleaning">
    <polygon points="128,122 210,122 140,168" fill="var(--teal-dark)"/>
    <polygon points="0,28 262,22 262,122 8,124" fill="var(--yellow)"/>
    <text class="discount-word" x="34" y="86">DISCOUNT</text>
    <text class="discount-sub" x="38" y="111">FOR THE FIRST CLEANING</text>
    <circle cx="211" cy="45" r="40" fill="var(--teal)"/>
    <text class="discount-pct" x="211" y="56" text-anchor="middle">30%</text>
  </svg>

  <p class="offer-note">We offer 30% off for the first cleaning to any new costumer with this post cards.</p>

  <div class="contact-band"></div>
  <div class="contact contact-phone">
    <svg viewBox="0 0 40 36" aria-hidden="true">
      <path d="M4 12 C4 4 36 4 36 12 L36 15 L28 15 L28 11 L12 11 L12 15 L4 15 Z" fill="var(--teal)"/>
      <path d="M10 16 L30 16 L35 33 L5 33 Z" fill="var(--teal)"/>
      <circle cx="20" cy="24" r="5" fill="var(--band)"/>
    </svg>
    <span>413-582-9174</span>
  </div>
  <div class="contact contact-email">
    <svg viewBox="0 0 40 36" aria-hidden="true">
      <path d="M3 14 L20 3 L37 14 V34 H3 Z" fill="var(--teal)"/>
      <rect x="9" y="12" width="22" height="18" fill="var(--white)"/>
      <text x="20" y="26" text-anchor="middle" font-family="Roboto Condensed, sans-serif" font-size="13" font-weight="700" fill="var(--teal)">@</text>
    </svg>
    <span>tidyhomesquad42@maplenest.com</span>
  </div>
</main>
</body>
</html>
```